Specialised investor in e-mobility and energy wants business card design

We need a business card design that fits our existing corporate design. <The look and feel must be 'sharp'/'clean', dynamic, communicate momentum, professionalism etc (as one would imagine from a firm in the financial sector). We like the idea of a reverse-side of the card that includes the logo, and the name and contact details on the other. We expect the deliverable to be whatever format might be required to be able to get cards printed directly by a service such as tandor press. Our website is www.orm.capital

```html
<!DOCTYPE html>
<html lang="en">
<head>
<meta charset="utf-8">
<title>ORM Capital – Business Card</title>
<link rel="stylesheet" href="https://fonts.googleapis.com/css2?family=Montserrat:wght@400;600&family=Questrial&display=swap">
<style>
  :root {
    --backdrop: #b3b3b3;
    --paper: #ffffff;
    --leaf: #8ab24d;
    --forest: #2f4d22;
    --ink: #3a3a3a;
  }
  * { margin: 0; padding: 0; box-sizing: border-box; }
  html, body {
    width: 1000px; height: 1200px; overflow: hidden;
    background: var(--backdrop);
  }
  .card {
    position: absolute; left: 51px; width: 898px; height: 539px;
    background: var(--paper); overflow: hidden;
  }
  .card--front { top: 44px; }
  .card--back { top: 617px; }
  .card__waves { position: absolute; inset: 0; width: 100%; height: 100%; }
  .wave--light { fill: var(--leaf); }
  .wave--dark { fill: var(--forest); }

  .contact {
    position: absolute; left: 507px; top: 142px;
    font-family: "Montserrat", sans-serif; color: var(--ink);
  }
  .contact__name { font-size: 26px; font-weight: 600; line-height: 34px; letter-spacing: 0.3px; }
  .contact__role { font-size: 28px; font-weight: 400; line-height: 38px; margin-bottom: 12px; }
  .contact__list { list-style: none; }
  .contact__item {
    display: flex; align-items: center; gap: 10px;
    height: 44px; font-size: 26px; letter-spacing: 0.3px;
  }
  .contact__icon { width: 28px; height: 28px; flex: none; }
  .contact__icon rect { fill: var(--forest); }
  .contact__icon .glyph { fill: none; stroke: #fff; stroke-width: 1.8; stroke-linecap: round; stroke-linejoin: round; }
  .contact__icon .glyph-fill { fill: #fff; }

  .brand {
    position: absolute; left: 0; right: 0; top: 232px;
    text-align: center;
    font-family: "Questrial", sans-serif; font-weight: 400;
    font-size: 86px; line-height: 96px; color: var(--forest);
    letter-spacing: 1px;
  }
</style>
</head>
<body>

<section class="card card--front">
  <svg class="card__waves" viewBox="0 0 1062 637" preserveAspectRatio="none" aria-hidden="true">
    <path class="wave--light" d="M0 0 H1062 V75 C980 45 900 30 820 35 C600 50 350 120 150 98 C90 92 40 85 0 78 Z"/>
    <path class="wave--dark" d="M0 560 C100 595 220 612 330 610 C560 605 760 530 900 536 C970 538 1020 548 1062 560 V637 H0 Z"/>
  </svg>

  <div class="contact">
    <p class="contact__name">Your Name</p>
    <p class="contact__role">Manager</p>
    <ul class="contact__list">
      <li class="contact__item">
        <svg class="contact__icon" viewBox="0 0 28 28" aria-hidden="true"><rect width="28" height="28" rx="3"/>
          <path class="glyph" d="M9 7 L12 7 L13 11 L11 12.5 C12 15 13.5 16.5 16 17.5 L17.5 15.5 L21 16.5 L21 19.5 C21 20.5 20 21 19 21 C13 20.5 8 15.5 7.5 9 C7.5 8 8 7 9 7 Z"/></svg>
        <span>123 444 555</span>
      </li>
      <li class="contact__item">
        <svg class="contact__icon" viewBox="0 0 28 28" aria-hidden="true"><rect width="28" height="28" rx="3"/>
          <path class="glyph" d="M14 19 C10 14.5 9 12.5 9 10.5 A5 5 0 0 1 19 10.5 C19 12.5 18 14.5 14 19 Z"/>
          <circle class="glyph" cx="14" cy="10.5" r="1.8"/>
          <path class="glyph" d="M9 22 H19"/></svg>
        <span>789 Your Street Here</span>
      </li>
      <li class="contact__item">
        <svg class="contact__icon" viewBox="0 0 28 28" aria-hidden="true"><rect width="28" height="28" rx="3"/>
          <rect class="glyph" x="6" y="8.5" width="16" height="11" style="fill:none"/>
          <path class="glyph" d="M6 8.5 L14 15 L22 8.5 M6 19.5 L11.5 13.5 M22 19.5 L16.5 13.5"/></svg>
        <span>info@yourname.com</span>
      </li>
      <li class="contact__item">
        <svg class="contact__icon" viewBox="0 0 28 28" aria-hidden="true"><rect width="28" height="28" rx="14"/>
          <circle class="glyph" cx="14" cy="14" r="8"/>
          <ellipse class="glyph" cx="14" cy="14" rx="3.5" ry="8"/>
          <path class="glyph" d="M6 14 H22 M7.5 10 H20.5 M7.5 18 H20.5"/></svg>
        <span>www.yourname.com</span>
      </li>
    </ul>
  </div>
</section>

<section class="card card--back">
  <svg class="card__waves" viewBox="0 0 1062 637" preserveAspectRatio="none" aria-hidden="true">
    <path class="wave--light" d="M0 0 H1062 V75 C1010 92 950 102 880 100 C650 95 450 20 230 26 C140 30 60 55 0 76 Z"/>
    <path class="wave--dark" d="M0 560 C60 545 120 536 190 537 C400 540 600 610 760 611 C900 612 1000 580 1062 560 V637 H0 Z"/>
  </svg>
  <p class="brand">ORM Capital</p>
</section>

</body>
</html>
```